Opening Titles for "Harbor of Kin" - Social Justice Feature Film

We are looking for a designer to design the opening titles for our social justice film "Harbor of Kin.” "Harbor of Kin" is the story of a separated mixed status and mixed ethnic family and their journey to reunite. You can see an early teaser of the film here (https://qrtmno.files.example/s/k52pd8vtwe103gm7b39kxrzs6q4j1n8w)(please note this is a TEASER NOT a trailer - it shows the story of only one of the family members in the teaser not all of them).
There is a mood board attached here that can help explain what we are looking for. A few things to keep in mind:
- We would like the Main Title "HARBOR OF KIN," to be in block letters with illustrated images that represent the town that two of the characters emigrate from and the culture/family life inside of the letters. "HARBOR OF KIN" title should be reminiscent of a particular kind of storytelling that comes from the coast of Oaxaca and Guerrero, particularly in the Afro-Mexico culture where we can see the storytelling in the artifacts as illustrated in the board. The images on the circle and the flsh plates are not just images, they are also telling a story and are reflective of a particular community. In the case of the film, at the start of the story, this family comes from an Afro-Mexican community.
- Please note where it says to double click on an image as that will lead to free ViewLoop videos that will give you a deeper sense of what we are looking for.
- As for the lettering of the titles/credits, with the exception of “HARBOR OF KIN” the font of everything else should look in the style of the “Oaxacan Old Fashioned” lettering.
- Each credit name/title should be in a different color that works well with the background image. A good example of this is the color of the credit with the woman in the hammock. (timecode: 1:01:20:18 in the Opening Credits/Titles clip: https://clip.example/7RtUoPaZ ). In this clip you can see that the yellow of the letters brings out the yellows and greens of the image behind it.
- Around each Credit name please frame it (however you choose to frame them) with a piece(s) of Mexican tile. The tile ideas are in the mood board and you can see something similar in the opening credits for “Walk a Quiet Mile” with the multicolored triangles. Double click on it in the mood board to see the “Walk a Quiet Mile” opening credits.
Here is a clip of the opening credits so that you can see where your design will go and how it will be used: https://clip.example/7RtUoPaZ

```html
<!DOCTYPE html>
<html lang="en">
<head>
<meta charset="utf-8">
<title>Harbor of Kin – Title Design Board</title>
<link rel="stylesheet" href="https://fonts.googleapis.com/css2?family=Lato:wght@400;700&family=Lilita+One&family=Montserrat:wght@500&family=Roboto:wght@500&display=swap">
<style>
  :root {
    --page: #ffffff;
    --panel: #222224;
    --ink: #111111;
    --red: #d9261c;
    --yellow: #f2a81d;
    --teal: #3f8391;
    --cream: #efdcb4;
    --aqua: #1aa6b3;
    --orange: #e8843a;
    --beach-top: #1c1b19;
    --beach-mid: #5d6468;
    --beach-low: #4a4641;
  }
  * { margin: 0; padding: 0; box-sizing: border-box; }
  html, body { width: 1200px; height: 842px; overflow: hidden; background: var(--page); }
  .board { position: relative; width: 1200px; height: 842px; }

  .frame { position: absolute; width: 583px; height: 328px; background: var(--panel); overflow: hidden; }
  .frame--title-dark { left: 12px; top: 14px; }
  .frame--title-scene { left: 606px; top: 14px; }
  .frame--superz { left: 12px; top: 390px; }
  .frame--lower-third { left: 607px; top: 390px; }

  .scene-backdrop {
    position: absolute; inset: 0;
    background: linear-gradient(180deg, var(--beach-top) 0%, var(--beach-top) 30%, var(--beach-mid) 50%, var(--beach-low) 72%, #3a3733 100%);
  }
  .timecode {
    position: absolute; left: 450px; top: 19px;
    font: 500 14px "Roboto", sans-serif; color: #ffffff; letter-spacing: 0.2px;
  }

  .title-art {
    position: absolute; left: 141px; top: 100px; width: 304px; height: 128px;
  }
  .title-art svg { display: block; width: 100%; height: 100%; }

  .superz {
    position: absolute; left: 0; right: 0; top: 136px;
    text-align: center; font: 19px/25px "Lilita One", sans-serif;
    letter-spacing: 0.3px; text-transform: uppercase;
  }
  .c-red { color: var(--red); }
  .c-yellow { color: var(--yellow); }
  .c-teal { color: var(--teal); }
  .c-cream { color: var(--cream); }

  .lower-third { position: absolute; left: 74px; top: 215px; }
  .lower-third__label { font: 500 12px "Montserrat", sans-serif; color: var(--orange); letter-spacing: 0.3px; }
  .lower-third__name { font: 26px/30px "Lilita One", sans-serif; color: var(--aqua); letter-spacing: 0.6px; margin-top: 1px; }

  .caption {
    position: absolute; font: 500 23px "Montserrat", sans-serif; color: var(--ink);
    transform: translateX(-50%); white-space: nowrap; letter-spacing: 0.4px;
  }
  .caption--opening { left: 600px; top: 346px; }
  .caption--superz { left: 303px; top: 720px; }
  .caption--lower-third { left: 906px; top: 720px; }

  .preview-link {
    position: absolute; left: 0; right: 0; top: 788px; text-align: center;
    font: 400 22px "Lato", sans-serif; color: var(--ink);
  }
  .preview-link a { font-weight: 700; color: var(--ink); text-decoration: none; margin-left: 10px; }
</style>
</head>
<body>
<main class="board">

  <section class="frame frame--title-dark">
    <div class="title-art" role="img" aria-label="Illustrated block-letter main title HARBOR OF KIN with folk scenes inside the letters, framed by zigzag borders">
      <svg viewBox="0 0 304 128" preserveAspectRatio="none" aria-hidden="true">
        <defs>
          <linearGradient id="title-tones-a" x1="0" x2="1" y1="0" y2="0">
            <stop offset="0" stop-color="#3f8391"/>
            <stop offset="0.35" stop-color="#d9261c"/>
            <stop offset="0.7" stop-color="#f2a81d"/>
            <stop offset="1" stop-color="#3f8391"/>
          </linearGradient>
        </defs>
        <rect x="0" y="0" width="304" height="128" rx="4" fill="url(#title-tones-a)" opacity="0.85"/>
      </svg>
    </div>
  </section>

  <section class="frame frame--title-scene">
    <div class="scene-backdrop" role="img" aria-label="Beach scene under a thatched palapa with plastic chairs, tables and the sea behind"></div>
    <p class="timecode">01:00:17:18</p>
    <div class="title-art" role="img" aria-label="Illustrated block-letter main title HARBOR OF KIN overlaid on the scene, framed by zigzag borders">
      <svg viewBox="0 0 304 128" preserveAspectRatio="none" aria-hidden="true">
        <defs>
          <linearGradient id="title-tones-b" x1="0" x2="1" y1="0" y2="0">
            <stop offset="0" stop-color="#3f8391"/>
            <stop offset="0.35" stop-color="#d9261c"/>
            <stop offset="0.7" stop-color="#f2a81d"/>
            <stop offset="1" stop-color="#3f8391"/>
          </linearGradient>
        </defs>
        <rect x="0" y="0" width="304" height="128" rx="4" fill="url(#title-tones-b)" opacity="0.85"/>
      </svg>
    </div>
  </section>

  <section class="frame frame--superz">
    <p class="superz">
      <span class="c-yellow">The</span> <span class="c-red">Ventura</span> <span class="c-teal">Family was just</span> <span class="c-cream">an</span> <span class="c-teal">Ameri</span><span class="c-yellow">can fa</span><span class="c-red">mily,</span><br>
      <span class="c-teal">Until</span> <span class="c-red">the day</span> <span class="c-teal">th</span><span class="c-cream">e</span><span class="c-red">y</span> <span class="c-teal">weren’t.</span>
    </p>
  </section>

  <section class="frame frame--lower-third">
    <div class="lower-third">
      <p class="lower-third__label">INTRODUCTION</p>
      <p class="lower-third__name">MARCO IBARRA</p>
    </div>
  </section>

  <p class="caption caption--opening">Opening title</p>
  <p class="caption caption--superz">Superz</p>
  <p class="caption caption--lower-third">Lower third</p>

  <p class="preview-link">Opening title - Motion preview <a href="https://drop.example/t-KQp47rrXNA">https://drop.example/t-KQp47rrXNA</a></p>

</main>
</body>
</html>
```